Letterhead to Prospective Clients

Create a letterhead (word & canva) that I will use to send letters to prospective clients and also include the Coralwood Estate Partners Logo, My Contact Details and Interchangeable "Suburb". Use the same font and colour pallete

Maris Dulworth | "Suburb" Specialist - Kestrel Bay & Surrounds
Mobile: 0417 862 095
Email: MD@CoralwoodEstatePartners.com.au

```html
<!DOCTYPE html>
<html lang="en">
<head>
<meta charset="utf-8">
<title>Coralwood Estate Partners Letterhead</title>
<link href="https://fonts.googleapis.com/css2?family=Josefin+Sans:wght@300&family=Arimo:wght@400;700&display=swap" rel="stylesheet">
<style>
  :root {
    --backdrop: #e6e7e9;
    --paper: #ffffff;
    --navy: #0d1b3e;
    --tan: #d4a87c;
    --ink: #3a3a3a;
  }
  * { margin: 0; padding: 0; box-sizing: border-box; }
  html, body {
    width: 1200px;
    height: 1200px;
    overflow: hidden;
    background: var(--backdrop);
  }
  .letterhead {
    position: absolute;
    left: 241.5px;
    top: 91.5px;
    width: 717px;
    height: 1017px;
    background: var(--paper);
    overflow: hidden;
  }
  .brand-name {
    position: absolute;
    top: 80px;
    left: 0;
    width: 100%;
    text-align: center;
    font-family: "Josefin Sans", sans-serif;
    font-weight: 300;
    font-size: 25px;
    line-height: 30px;
    letter-spacing: 0.1em;
    color: var(--navy);
    text-transform: uppercase;
  }
  .footer-shapes {
    position: absolute;
    left: 0;
    top: 0;
    width: 717px;
    height: 1017px;
  }
  .contact {
    position: absolute;
    left: 0;
    width: 100%;
    text-align: center;
    font-family: "Arimo", Arial, sans-serif;
  }
  .contact-name {
    top: 919px;
    font-size: 20px;
    font-weight: 700;
    color: var(--navy);
  }
  .contact-role {
    top: 949px;
    font-size: 13px;
    color: var(--ink);
  }
  .contact-details {
    top: 970px;
    font-size: 13px;
    color: var(--ink);
    word-spacing: 1px;
  }
  .divider { margin: 0 14px; }
</style>
</head>
<body>
  <main class="letterhead">
    <div class="brand-name">Coralwood Estate Partners</div>

    <svg class="footer-shapes" viewBox="0 0 717 1017" aria-hidden="true">
      <rect class="accent-bar-left" x="0" y="946.5" width="40.5" height="9" fill="var(--tan)"/>
      <rect class="accent-bar-right" x="676.5" y="946.5" width="40.5" height="9" fill="var(--tan)"/>
      <rect class="base-band" x="0" y="1005" width="717" height="12" fill="var(--tan)"/>
      <polygon class="corner-left" points="0,967.5 70.5,967.5 103.5,1017 0,1017" fill="var(--navy)"/>
      <polygon class="corner-right" points="643.5,967.5 717,967.5 717,1017 610.5,1017" fill="var(--navy)"/>
    </svg>

    <p class="contact contact-name">Maris Dulworth</p>
    <p class="contact contact-role">"Suburb" Specialist - Kestrel Bay &amp; Surrounds</p>
    <p class="contact contact-details">M: 0417 862 095<span class="divider">|</span>E: MD@CoralwoodEstatePartners.com.au</p>
  </main>
</body>
</html>
```